Hey,
My name is Tomas Brevilacqua and I'm starting a PhD in Physics next year. I want to a bit more than just research on my own. I want to bring some public involvement to it.
"Zeta Quanta" is website/pressmoor/blog. It is a way to bring physics to the general public without losing the math or the physics essence - This is a place to share fun and interesting findings that PhD students, Professors, High school students and basically everyone else that loves and wants to know a bit more about nature. The idea is to put real science to debate in a open non-judgmental way in prol of knowledge and discovery. "Everybody" is welcome to post relevant things such as experiments made at home as well as their latest discovery in their super high tech £100M lab.
The first step of the project is to develop a BLOG (Pressmoor) - the domain is already register "zetaquanta.org and zetaquanta.com" that could host that initial debate and posts.
Think http://lumenvault.org/ ; http://www.hollowtide.org/; https://www.youtube.com/user/brambleglyphs; https://www.youtube.com/user/quirkvector as a guidelines...
http://trelvanix.pombo.com.br/
I would enjoy touches of watercolour design here and there.
I also like pastel colours. But remember, I am a scientist and not at all designer. I'll trust the artists to create and show me what they are up to.
UPDATE: Just so you guys know. I want to do a Website in form of a Blog. I want to easily post and upload videos and articles related to Physics.
I'm more familiar with Pressmoor but if you say that any other platform does the job better and I can still maintain the domain zetaquanta.org lets do it!
Updates
Update number 2: I will respond every designer asap. I will however do that between 9:00am and 14:00 pm Brasilia/Brazil Time.
So please don't get upset or take it personal if you don't get a feedback right away, specially if it is 02:00 a.m my time, ok ?! : - )
Thanks Guys and good work!
For all designers that just want to do logos please post them in: Manage Project | Zeta Quanta - Logo Design Project
We will continue from there!
Target Market(s)
Everyone that likes physics, no matter if you are a Halvard Medalist or a single mother that likes physics.
Industry/Entity Type
Artists
Font styles to use
Other font styles liked:
- I like Calibri, Helvetica, Verdana, Univers and Tahoma for body text, Sometimes I use Arial. Cambria and Georgia for headings
Requirements
Must have
- I'm open minded! But I like thinks to be simple!
Nice to have
- The way you going to put "Zeta Quanta" is completely up to you. I usually like it simple but. Show me what you got and I'll give you feedback if I like it or not! Just remember to keep it clean and user friendly.
Should not have
- Just try beautiful and functional designs. I usually don't like super old style fonts like Times New Roman and very elaborate things that are hard to read.

```html
<!DOCTYPE html>
<html lang="en">
<head>
<meta charset="utf-8">
<title>Zeta Quanta</title>
<link href="https://fonts.googleapis.com/css2?family=Open+Sans:ital,wght@0,400;0,600;0,700;1,400;1,600&family=PT+Serif:wght@400;700&display=swap" rel="stylesheet">
<style>
:root{
  --ink:#222222;
  --header:#232323;
  --red:#f04e53;
  --band:#c41f2e;
  --panel:#efefef;
  --panel-line:#dcdcdc;
  --muted:#8a8a8a;
  --footer:#e6e6e6;
  --yellow:#f5c400;
  --white:#ffffff;
}
*{box-sizing:border-box;margin:0;padding:0}
html,body{width:1200px;height:2276px;overflow:hidden}
body{position:relative;background:var(--white);font-family:"Open Sans",Arial,sans-serif;color:var(--ink)}
a{color:inherit;text-decoration:none}

.site-header{position:absolute;left:0;top:0;width:1200px;height:73px;background:var(--header)}
.brand{position:absolute;left:100px;top:14px;font-family:"PT Serif",Georgia,serif;font-size:33px;color:var(--white);font-weight:400}
.main-nav{position:absolute;left:511px;top:24px;display:flex;gap:0}
.main-nav a{display:block;height:25px;line-height:25px;font-size:13px;color:var(--white);padding:0 13px;margin-right:7px}
.main-nav a.active{background:var(--red);width:76px;text-align:center;border-radius:2px;margin-right:2px}

.hero{position:absolute;left:100px;top:118px;width:1000px;height:504px;background:var(--white)}
.hero-row{display:grid;gap:1px;height:251px}
.hero-row.top{grid-template-columns:repeat(3,1fr)}
.hero-row.bottom{grid-template-columns:repeat(4,1fr);margin-top:1px;height:252px}
.tile{position:relative;overflow:hidden}
.tile .caption{position:absolute;left:22px;right:18px;bottom:24px;color:var(--white);font-weight:600;font-size:19px;line-height:25px}
.hero-row.bottom .caption{font-size:15px;line-height:20px;left:16px;bottom:22px}
.ph-a{background:linear-gradient(180deg,#4a4d52,#1c1d20)}
.ph-b{background:linear-gradient(160deg,#2a3036,#0c0f12)}
.ph-c{background:linear-gradient(180deg,#505355,#1d1e1f)}
.ph-d{background:linear-gradient(160deg,#1e5a45,#0f2a22)}
.ph-e{background:linear-gradient(160deg,#14424f,#061318)}
.ph-f{background:linear-gradient(180deg,#2a2a2a,#0e0e0e)}
.ph-g{background:linear-gradient(180deg,#3a3f47,#18191b)}

.panel{position:absolute;background:var(--panel);border:1px solid var(--panel-line)}
.article{left:100px;top:669px;width:663px;height:863px}
.article-title{position:absolute;left:24px;top:20px;width:600px;font-family:"PT Serif",Georgia,serif;font-weight:700;font-size:28px;line-height:35px;text-transform:uppercase;color:#232323;letter-spacing:.3px}
.article-meta{position:absolute;left:24px;right:24px;top:104px;border-top:1px solid var(--panel-line);padding-top:8px;font-size:9px;color:var(--muted);display:flex;align-items:center}
.article-meta .share{margin-left:auto;display:flex;gap:7px;align-items:center}
.dot{width:6px;height:6px;background:#555;border-radius:50%}
.article-photo{position:absolute;left:24px;top:154px;width:615px;height:325px;background:linear-gradient(90deg,#2e6b3c 0%,#cfcfc7 40%,#e9e7e1 60%,#2f6b3d 100%)}
.article-sub{position:absolute;left:24px;top:500px;font-size:17px;color:#222}
.article-body{position:absolute;left:24px;width:615px;font-size:11.5px;line-height:19px;color:var(--muted)}
.p1{top:534px}.p2{top:628px}
.btn{display:block;background:var(--red);color:var(--white);text-align:center;border-radius:2px}
.article .btn{position:absolute;left:24px;top:803px;width:615px;height:30px;line-height:30px;font-size:12px}

.videos{left:100px;top:1555px;width:663px;height:259px}
.video-main{position:absolute;left:23px;top:22px;width:393px;height:215px;background:linear-gradient(90deg,#2b2b2b,#4a4642 60%,#2a2826)}
.video-thumb{position:absolute;left:436px;width:200px;height:61px}
.vt1{top:22px;background:linear-gradient(90deg,#a6744d,#d6b48c,#6b5440)}
.vt2{top:98px;background:linear-gradient(90deg,#d8d8d8,#f1f1f1,#7a6a5c)}
.vt3{top:174px;background:linear-gradient(90deg,#5e4a3a,#a88c6b,#3a3028)}
.play{position:absolute;left:50%;top:50%;transform:translate(-50%,-50%);background:rgba(20,20,20,.85);display:flex;align-items:center;justify-content:center}
.video-main .play{width:80px;height:46px}
.video-thumb .play{width:56px;height:28px}

.promo{position:absolute;left:795px;top:669px;width:305px;height:176px;background:linear-gradient(180deg,#2a2a2a,#1a1a1a 60%,#33302a);color:var(--white);text-align:center;overflow:hidden}
.promo .ribbon{position:absolute;left:-24px;top:10px;width:90px;height:18px;background:var(--red);transform:rotate(-45deg);font-size:8px;line-height:18px;font-weight:700}
.promo .kicker{position:absolute;top:42px;width:100%;font-size:11px}
.promo .headline{position:absolute;top:60px;width:100%;font-family:"PT Serif",Georgia,serif;font-weight:700;font-size:26px;letter-spacing:1px}
.promo .sub{position:absolute;top:104px;width:100%;font-size:10px;font-weight:600}

.side-title{position:absolute;left:21px;right:21px;top:14px;padding-bottom:10px;border-bottom:1px solid var(--panel-line);font-family:"PT Serif",Georgia,serif;font-weight:700;font-size:18px;color:#222}
.articles{left:795px;top:862px;width:305px;height:461px}
.art-item{position:absolute;left:21px;width:263px;height:124px}
.art-item span{position:absolute;left:14px;bottom:14px;color:var(--white);font-family:"PT Serif",Georgia,serif;font-weight:700;font-size:14px;text-decoration:underline}
.ai1{top:64px;background:linear-gradient(180deg,#2e6e4a,#1d4b33)}
.ai2{top:188px;background:linear-gradient(90deg,#3c3c44,#6a6a72,#3a3640)}
.ai3{top:312px;height:124px;background:linear-gradient(180deg,#2e4a6a,#162438)}

.news{left:795px;top:1342px;width:305px;height:471px}
.news-item{position:absolute;left:21px;right:21px;height:96px;border-bottom:1px solid var(--panel-line)}
.news-thumb{position:absolute;left:0;top:0;width:66px;height:66px}
.news-item h4{position:absolute;left:76px;top:0;font-size:14px;font-weight:600;line-height:19px;color:#333}
.news-info{position:absolute;left:76px;top:44px;display:flex;align-items:center;gap:8px;font-size:10px;color:var(--muted)}
.badge{display:inline-flex;align-items:center;gap:4px;height:14px;padding:0 5px;background:var(--band);color:var(--white);font-size:9px;border-radius:1px}
.badge.grey{background:#cfcfcf}
.n1{top:60px}.n2{top:156px}.n3{top:252px}.n4{top:350px;border-bottom:none}
.t1{background:linear-gradient(135deg,#f0b04a,#c97a2a)}
.t2{background:linear-gradient(135deg,#e6e6e6,#6a5a52)}
.t3{background:linear-gradient(135deg,#6aa640,#8a5a30)}
.t4{background:linear-gradient(135deg,#8ab2d6,#3c4a5c)}
.news .btn{position:absolute;left:21px;right:21px;top:432px;height:24px;line-height:24px;font-size:11px}

.tweet-band{position:absolute;left:0;top:1889px;width:1200px;height:50px;background:var(--band);color:var(--white);display:flex;align-items:center;padding-left:102px}
.tweet-band .label{font-size:19px;margin-right:14px}
.tweet-band .dot-w{width:8px;height:8px;background:var(--white);border-radius:50%;margin-right:6px}
.tweet-band .msg{font-style:italic;font-weight:600;font-size:14px}

.site-footer{position:absolute;left:0;top:1939px;width:1200px;height:270px;background:var(--footer)}
.fcol{position:absolute;top:24px}
.fcol h3{font-size:16px;font-weight:400;color:#222;text-transform:uppercase}
.subscribe{left:100px;width:260px}
.subscribe p{font-size:12px;line-height:20px;color:#444;margin-top:22px}
.subscribe .label{margin-top:18px}
.sub-form{display:flex;margin-top:6px}
.sub-form .field{width:152px;height:34px;background:var(--white)}
.sub-form .go{width:100px;height:34px;background:var(--yellow);font-size:12px;line-height:34px;text-align:center;color:#222}
.blogroll{left:473px;width:251px}
.blogroll ul{list-style:none;margin-top:18px;border-top:1px solid #c9c9c9}
.blogroll li{height:45.5px;line-height:45px;border-bottom:1px solid #c9c9c9;font-size:12px;color:#555}
.contact{left:848px;width:252px}
.contact ul{list-style:none;margin-top:14px;border-top:1px solid #c9c9c9}
.contact li{display:flex;align-items:center;gap:14px;border-bottom:1px solid #c9c9c9;font-size:13px;color:#111}
.contact li.phone{height:52px}
.contact li.addr{height:60px;line-height:16px;font-size:12px}
.contact li.mail{height:45px;font-size:12px;font-weight:600}

.copyright{position:absolute;left:0;top:2209px;width:1200px;height:67px;background:#0d0d0d;color:var(--white);text-align:center;line-height:67px;font-size:15px}
</style>
</head>
<body>

<header class="site-header">
  <div class="brand">Zeta Quanta</div>
  <nav class="main-nav">
    <a class="active" href="#">Home</a>
    <a href="#">About Us</a>
    <a href="#">Experiments</a>
    <a href="#">Topics</a>
    <a href="#">Gallery</a>
    <a href="#">Articles</a>
    <a href="#">Contact Us</a>
  </nav>
</header>

<section class="hero">
  <div class="hero-row top">
    <div class="tile ph-a" role="img" aria-label="Scientist with glasses working in a laboratory"><p class="caption">Sed ut perspiciatis unde omnis iste error sit</p></div>
    <div class="tile ph-b" role="img" aria-label="Molecular model of spheres and rods on dark background"><p class="caption">Nemo enim ipsam quia voluptas sit aspernatur aut odit autro</p></div>
    <div class="tile ph-c" role="img" aria-label="Young man in front of a chalkboard reading science"><p class="caption">Nemo enim ipsam quia voluptas sit aut odit aut fugit sed</p></div>
  </div>
  <div class="hero-row bottom">
    <div class="tile ph-d" role="img" aria-label="Lecturer in front of green chalkboard"><p class="caption">Neque porro qui dolorem ipsum quia dolor sit amet sed</p></div>
    <div class="tile ph-e" role="img" aria-label="Researcher among blue lit laboratory equipment"><p class="caption">who loves or pursues or desires to obtain pain of itself</p></div>
    <div class="tile ph-f" role="img" aria-label="Blackboard covered in physics equations"><p class="caption">but because in which toil and pain can procure him some</p></div>
    <div class="tile ph-g" role="img" aria-label="Test tubes in a rack beside an apple"><p class="caption">Ut enim ad minima veniam, quis nostrum laboriosam</p></div>
  </div>
</section>

<article class="panel article">
  <h1 class="article-title">Itaque earum rerum hic tenetur a sapiente delectus</h1>
  <div class="article-meta">
    <span>7630 Views / Posted Jan 3, 2014 &nbsp;|&nbsp; Comments</span>
    <span class="share"><span class="dot"></span><span class="dot"></span><span class="dot"></span><span class="dot"></span></span>
  </div>
  <div class="article-photo" role="img" aria-label="Smiling teacher with arms crossed in front of a green chalkboard"></div>
  <h2 class="article-sub">Sed ut perspiciatis unde omnis iste natus error sit</h2>
  <p class="article-body p1">voluptatem accusantium doloremque laudantium, totam rem aperiam, eaque ipsa quae ab illo inventore veritatis et quasi architecto beatae vitae dicta sunt explicabo. Nemo enim ipsam voluptatem quia voluptas sit aspernatur aut odit aut fugit, sed quia consequuntur magni dolores eos qui ratione voluptatem sequi nesciunt. Neque porro quisquam est, qui dolorem ipsum quia dolor sit amet, consectetur, adipisci velit sed.</p>
  <p class="article-body p2">Neque porro quisquam est, qui dolorem ipsum quia dolor sit amet, consectetur, adipisci velit, sed quia non numquam eius modi tempora incidunt ut labore et dolore magnam aliquam quaerat voluptatem. Ut enim ad minima veniam, quis nostrum exercitationem ullam corporis suscipit laboriosam, nisi ut aliquid ex ea commodi consequatur Quis autem vel eum iure reprehenderit qui in ea voluptate velit esse quam nihil molestiae consequatu similique sunt in culpa qui officia deserunt mollitia animi, id est laborum et dolorum fuga. Et harum quidem rerum facilis est et expedita distinctio. Nam libero tempore, cum soluta nobis est eligendi optio cumque nihil impedit quo minus id quod maxime placeat facere possimus</p>
  <a class="btn" href="#">Read More</a>
</article>

<section class="panel videos">
  <div class="video-main" role="img" aria-label="Video still of a professor at a blackboard">
    <span class="play"><svg width="12" height="14" viewBox="0 0 12 14"><path d="M0 0L12 7L0 14Z" fill="#fff"/></svg></span>
  </div>
  <div class="video-thumb vt1" role="img" aria-label="Video still of students in a classroom"><span class="play"><svg width="10" height="12" viewBox="0 0 12 14"><path d="M0 0L12 7L0 14Z" fill="#fff"/></svg></span></div>
  <div class="video-thumb vt2" role="img" aria-label="Video still of a teacher at a whiteboard"><span class="play"><svg width="10" height="12" viewBox="0 0 12 14"><path d="M0 0L12 7L0 14Z" fill="#fff"/></svg></span></div>
  <div class="video-thumb vt3" role="img" aria-label="Video still of a lecture hall"><span class="play"><svg width="10" height="12" viewBox="0 0 12 14"><path d="M0 0L12 7L0 14Z" fill="#fff"/></svg></span></div>
</section>

<aside class="promo" role="img" aria-label="Banner over a dim laboratory scene">
  <span class="ribbon">NEW'S</span>
  <p class="kicker">LOREM IPSUM DOLOR</p>
  <p class="headline">SIT VOLUPTATEM</p>
  <p class="sub">NEMO IPSAM VOLUPTATEM VOLUPTAS</p>
</aside>

<section class="panel articles">
  <h3 class="side-title">ARTICLES</h3>
  <a class="art-item ai1" href="#" role="img" aria-label="Lecturer in suit at a chalkboard"><span>Pursue pleasure rationally</span></a>
  <a class="art-item ai2" href="#" role="img" aria-label="Woman smiling in a gallery"><span>Who do not know how ?</span></a>
  <a class="art-item ai3" href="#" role="img" aria-label="Smiling woman on blue background"><span>Dolorem ipsum quia dolor sit</span></a>
</section>

<section class="panel news">
  <h3 class="side-title">NEW'S</h3>
  <div class="news-item n1">
    <div class="news-thumb t1" role="img" aria-label="Food item on orange background"></div>
    <h4>See what is actually healty,<br>you wont believe it</h4>
    <div class="news-info"><span class="badge grey">&#9633; 0</span>-<span>AUGUST 11, 2014</span></div>
  </div>
  <div class="news-item n2">
    <div class="news-thumb t2" role="img" aria-label="Snow machine on a ski slope"></div>
    <h4>Ski season is comming,<br>prepare yourself</h4>
    <div class="news-info"><span class="badge">&#9633; 1</span>-<span>AUGUST 11, 2014</span></div>
  </div>
  <div class="news-item n3">
    <div class="news-thumb t3" role="img" aria-label="Plate of food on green background"></div>
    <h4>The most delicios food is<br>not always that healty</h4>
    <div class="news-info"><span class="badge">&#9633; 1</span>-<span>AUGUST 11, 2014</span></div>
  </div>
  <div class="news-item n4">
    <div class="news-thumb t4" role="img" aria-label="City skyline"></div>
    <h4>New people are comming<br>this week in the city</h4>
    <div class="news-info"><span class="badge">&#9633; 1</span>-<span>AUGUST 11, 2014</span></div>
  </div>
  <a class="btn" href="#">Read More</a>
</section>

<div class="tweet-band">
  <span class="label">Chirpline</span>
  <span class="dot-w"></span>
  <span class="msg">: Lorem ipsum dolor sit amet, consectetur adipisicing elit, sed do eiusmod tempor incididunt ut labore et dolore magna aliqua.</span>
</div>

<footer class="site-footer">
  <div class="fcol subscribe">
    <h3>Subscribe</h3>
    <p>Aametu dolor sit amet, setetr sadipsceitr,<br>sed diam nonumy eirmod tempor<br>labore.magna aliquyam orem ipsum.</p>
    <p class="label">Enter your email below:</p>
    <div class="sub-form"><span class="field"></span><span class="go">SUBSCRIBE</span></div>
  </div>
  <div class="fcol blogroll">
    <h3>Blog Roll</h3>
    <ul>
      <li>Making money forum</li>
      <li>Making money forum</li>
      <li>Making money forum</li>
      <li>Making money forum</li>
    </ul>
  </div>
  <div class="fcol contact">
    <h3>Contact Info</h3>
    <ul>
      <li class="phone"><svg width="14" height="16" viewBox="0 0 14 16"><rect x="2" y="0" width="10" height="16" rx="1.5" fill="#111"/><rect x="4" y="2" width="6" height="6" fill="#e6e6e6"/><rect x="4" y="10" width="2" height="1.5" fill="#e6e6e6"/><rect x="8" y="10" width="2" height="1.5" fill="#e6e6e6"/><rect x="4" y="12.5" width="2" height="1.5" fill="#e6e6e6"/><rect x="8" y="12.5" width="2" height="1.5" fill="#e6e6e6"/></svg>012 4455 6170</li>
      <li class="addr"><svg width="16" height="15" viewBox="0 0 16 15"><path d="M8 0L16 7H13.5V15H9.5V10H6.5V15H2.5V7H0Z" fill="#111"/></svg><span>Lorem Lipsum,<br>Street No. 4569</span></li>
      <li class="mail"><svg width="16" height="11" viewBox="0 0 16 11"><rect width="16" height="11" fill="#111"/><path d="M0 0L8 6L16 0" stroke="#e6e6e6" stroke-width="1.2" fill="none"/></svg>info@zetaquanta.com</li>
    </ul>
  </div>
</footer>

<div class="copyright">© 2014 Zeta Quanta.com All rights reserved.</div>

</body>
</html>
```